VarnLink Signal Systems Website Design

We are an Australian based telecommunications company who specialise in the design, build and implementation of mission critical communications infrastructure. We have offices throughout Australia, New Zealand and Europe. Our Customers are operators in multiple markets from Oil & Gas, Mining, Government, Utilities, Carrier & Transportation.

We also work with large multi-national companies, that provide telecommunication and services such as; Pelvaro, Dransvik, Quorba, Talmoss and many more. We want to be able to achieve the same level of impressions and professionalism as what these companies present on their websites.

To reflect our recent move into the European market, we need our new site to reflect who we are as a company, and exhibit the fact we are not just based in Australia, but we are a global organisation. We want to have a fresh clean look, thats modern, dynamic and simple. Flat textures and colours are perfect for us to adapt to. A site that is based around content management, with a responsive design that can be used on all devices.

We have started to develop a basic design language that we would like to incorporate in our overall website design. We have attached some documents that highlight our design language and we can provide colour codes and fonts to ensure consistency.

Our existing site is: www.varnlinkss.example. Please feel free to view and pick apart items. From this example, we would massive improvement in how the site looks, feels and functions. We also want social media to form a big part of our site, with the likes of posts from chirpnet and blogs posting capabilities.

If you require anymore information about VarnLink or our requirements, please do not hesitate to contact.

Thanks and good luck!

Target Market(s)

Potential & Existing Customers, New international customers & markets, New Market Sectors, Partners, Service Providers

Industry/Entity Type

Telecommunications

Coding

Coded - Design and coding required

Number of Pages Required

5+ page

Font styles to use
Sans Serif

Requirements
Must have
• Content Management, Responsive Design for multiple device compatibility, Social media integration, use of lots of imagery, drop down menus, search capabilities
Should not have
• No flash.

```html
<!DOCTYPE html>
<html lang="en">
<head>
<meta charset="utf-8">
<title>VarnLink Signal Systems</title>
<link href="https://fonts.googleapis.com/css2?family=Open+Sans:wght@400;600;700&family=Oswald:wght@400;500&display=swap" rel="stylesheet">
<style>
:root{
  --ink:#333;
  --muted:#666;
  --accent:#6a6fc4;
  --nav:#6e6e6e;
  --subnav:#474747;
  --band:#e4e4e4;
  --footer:#2b2b2b;
  --footer-col:#3a3a3a;
  --white:#fff;
}
*{box-sizing:border-box;margin:0;padding:0}
html,body{width:1200px;height:2552px;overflow:hidden}
body{font-family:"Open Sans",Arial,sans-serif;color:var(--ink);background:var(--white);font-size:13px;line-height:1.6}
.wrap{width:1000px;margin:0 auto;position:relative}
ul{list-style:none}

.site-header{height:88px}
.site-header .wrap{height:88px;display:flex;align-items:center;justify-content:space-between}
.brand{display:flex;align-items:center;gap:10px;font-weight:700;font-size:26px;color:var(--subnav)}
.brand-mark{width:16px;height:16px;background:var(--accent);border-radius:50%}
.header-info{display:flex;gap:26px;font-size:10px;color:var(--muted);align-items:flex-start}
.header-info strong{display:block;color:var(--ink);font-size:10px}
.search{margin-top:22px}

.main-nav{height:34px;background:var(--nav)}
.main-nav ul{display:flex;height:34px;align-items:center;gap:30px}
.main-nav a{color:var(--white);font-size:12px;font-weight:600;text-decoration:none;text-transform:uppercase}
.sub-nav{height:28px}
.sub-nav ul{width:800px;height:28px;background:var(--subnav);display:flex;align-items:center;gap:26px;padding-left:14px}
.sub-nav a{color:#ddd;font-size:11px;text-decoration:none}
.sub-nav a.active{color:var(--white);font-weight:600}

.hero{height:390px;background:linear-gradient(180deg,#3d5f9a 0%,#5a82bd 45%,#8a7a66 72%,#a4886a 100%);display:flex;flex-direction:column;align-items:center;justify-content:center;color:var(--white);text-align:center}
.hero h1{font-family:"Oswald",Arial,sans-serif;font-weight:500;font-size:64px;letter-spacing:3px;line-height:1.1;margin-top:80px}
.hero p{font-size:15px;margin-top:6px}

.tag{display:inline-block;background:var(--accent);color:var(--white);font-family:"Oswald",Arial,sans-serif;font-size:32px;font-weight:500;padding:0 14px;line-height:1.3;letter-spacing:1px}
.tag-after{font-family:"Oswald",Arial,sans-serif;font-size:32px;color:var(--ink)}

.about{height:370px;padding-top:45px}
.about .row{display:flex;gap:60px;margin-top:28px}
.about .copy{width:430px}
.about .copy p{margin-bottom:14px;color:var(--muted)}
.photo{display:block}
.about .photo{width:420px;height:230px;background:linear-gradient(160deg,#7fa7d6,#b9c6d4 55%,#8d8f95)}

.vision{height:170px;text-align:center}
.vision h2{font-family:"Oswald",Arial,sans-serif;font-size:34px;font-weight:400;color:var(--ink)}
.vision h2 span{color:var(--accent)}
.vision p{font-weight:600;font-size:13px;margin-top:6px}

.tech{height:300px;padding-top:20px}
.tech .row{display:flex;gap:60px}
.tech .photo{width:440px;height:260px;background:linear-gradient(150deg,#c9d3dc,#8ea6b9 60%,#5c6e80)}
.tech .copy{width:500px;color:var(--muted)}
.tech .copy p{margin-top:12px}
.tech .copy .lead{color:var(--ink);font-weight:600}
.ticks{display:flex;gap:80px;margin-top:10px}
.ticks li{padding-left:14px;position:relative}
.ticks li::before{content:"";position:absolute;left:0;top:8px;width:5px;height:5px;border-radius:50%;background:var(--accent)}

.markets{height:470px;padding-top:40px}
.markets .row{display:flex;gap:50px}
.markets .copy{width:520px;color:var(--muted)}
.markets .copy p{margin-top:18px}
.sectors{display:grid;grid-template-columns:200px 200px;margin-top:22px;row-gap:4px}
.sectors li{padding-left:14px;position:relative}
.sectors li::before{content:"";position:absolute;left:0;top:8px;width:5px;height:5px;border-radius:50%;background:var(--accent)}
.gallery{display:grid;grid-template-columns:205px 205px;gap:10px;margin-top:10px}
.gallery .photo{height:160px}
.g1{background:linear-gradient(160deg,#3a4a5f,#c56a2a)}
.g2{background:linear-gradient(160deg,#7b9bc0,#a98a62)}
.g3{background:linear-gradient(160deg,#5e7aa3,#c49a5a)}
.g4{background:linear-gradient(160deg,#90b2d3,#6e7c4c)}

.partners{height:290px;background:var(--band);text-align:center;padding-top:40px}
.partners h2{font-family:"Oswald",Arial,sans-serif;font-weight:400;font-size:36px;color:var(--accent)}
.partner-list{display:flex;justify-content:center;gap:18px;margin-top:50px}
.partner-list li{width:176px;height:88px;background:var(--white);display:flex;align-items:center;justify-content:center;font-weight:700;font-size:20px;color:var(--subnav)}

.site-footer{height:412px;background:var(--footer);color:#bbb;font-size:11px}
.site-footer .wrap{display:flex;height:412px}
.footer-brand{width:320px;padding-top:40px}
.footer-brand .brand{color:var(--white);font-size:24px}
.contact{margin-top:40px}
.contact li{display:flex;align-items:center;gap:10px;margin-bottom:14px}
.footer-cols{flex:1;display:flex;background:var(--footer-col);padding:36px 0 0 30px;gap:30px}
.footer-cols div{width:150px}
.footer-cols h3{color:var(--white);font-size:14px;font-weight:600;margin-bottom:16px}
.footer-cols li{margin-bottom:10px}
</style>
</head>
<body>

<header class="site-header">
  <div class="wrap">
    <div class="brand"><span class="brand-mark"></span>VarnLink</div>
    <div class="header-info">
      <div><strong>OFFICE AUSTRALIA</strong>48 Harwell Drive<br>+61 3 5550 0142</div>
      <div><strong>OFFICE UNITED KINGDOM</strong>7 Rolston Way, Leeds<br>+44 113 555 0188</div>
      <div>info@varnlinkss.example<br>www.varnlinkss.example</div>
      <svg class="search" width="16" height="16" viewBox="0 0 16 16" aria-label="Search"><circle cx="6.5" cy="6.5" r="5" fill="none" stroke="#333" stroke-width="2"/><line x1="10.5" y1="10.5" x2="15" y2="15" stroke="#333" stroke-width="2"/></svg>
    </div>
  </div>
</header>

<nav class="main-nav">
  <div class="wrap">
    <ul>
      <li><a href="#">Home</a></li>
      <li><a href="#">Products Services</a></li>
      <li><a href="#">Sectors</a></li>
      <li><a href="#">Support</a></li>
      <li><a href="#">Corporate</a></li>
      <li><a href="#">Blog</a></li>
      <li><a href="#">Contact</a></li>
    </ul>
  </div>
</nav>
<nav class="sub-nav">
  <div class="wrap">
    <ul>
      <li><a href="#">Partners</a></li>
      <li><a href="#">CDMA 450</a></li>
      <li><a href="#">Rapid Site Solution</a></li>
      <li><a href="#">Training</a></li>
      <li><a href="#">Technical Support</a></li>
      <li><a href="#" class="active">Professional Services</a></li>
    </ul>
  </div>
</nav>

<section class="hero" role="img" aria-label="Solar-powered communications tower on a remote site under a blue sky">
  <h1>WHATEVER THE ENIVROMENT</h1>
  <p>Quickly deploy communications infrastructure in the most</p>
</section>

<section class="about">
  <div class="wrap">
    <h2><span class="tag">ABOUT</span> <span class="tag-after">| VarnLink</span></h2>
    <div class="row">
      <div class="copy">
        <p>VarnLink Signal Systems is an Australian owned company that provides turnkey communications networks to customers around the world. Founded in 1998, the company has grown to be the leading supplier of communications systems and equipment in its field.</p>
        <p>Our core business covers the utilities and carrier markets, and have succeeded in expanding our profile into the emergency services sector.</p>
        <p>As a leading international provider of communications design, supply, integration and support in the dedicated and industrial networks sector, we have unsurpassed experience and knowledge that our customers rely on.</p>
      </div>
      <div class="photo" role="img" aria-label="Modern glass office building"></div>
    </div>
  </div>
</section>

<section class="vision">
  <div class="wrap">
    <h2>Our <span>Vision</span></h2>
    <p>To be a leading international provider of advanced and engineered solutions for mission and business critical networks.</p>
    <p>These are delivered through partnership with customers, a highly skilled workforce, excellence in professional services and innovation.</p>
  </div>
</section>

<section class="tech">
  <div class="wrap row">
    <div class="photo" role="img" aria-label="Support team meeting around a table in a bright office"></div>
    <div class="copy">
      <h2><span class="tag">TECHNICAL SUPPORT</span></h2>
      <p>VarnLink offers flexible multi-technology and multi-vendor support services. We take an end to end view of networks, helping you to resolve issues quickly and completely. Our specialised expertise in building and supporting critical communications infrastructure gives VarnLink the experience to solve your network problems.</p>
      <p class="lead">With our in depth knowledge and understanding of your network, we can help your technical team with:</p>
      <ul class="ticks">
        <li>Diagnostic<br>guidance</li>
        <li>Setting up for optimum<br>performance</li>
      </ul>
    </div>
  </div>
</section>

<section class="markets">
  <div class="wrap row">
    <div class="copy">
      <h2><span class="tag">MARKET SECTORS</span></h2>
      <p>VarnLink develops systems and networks to meet the stringent requirements of mission critical industries. These sectors are undergoing a process of evolution, from existing legacy requirements to a range of next generation applications. In most cases, this necessitates substantially higher bandwidths and a review of the overall network architecture.</p>
      <ul class="sectors">
        <li>Oil &amp; Gas</li><li>Mining</li>
        <li>Utilities</li><li>Carrier</li>
        <li>Transport</li><li>Emergency Services</li>
      </ul>
    </div>
    <div class="gallery">
      <div class="photo g1" role="img" aria-label="Oil refinery at dusk"></div>
      <div class="photo g2" role="img" aria-label="Open cut mining site"></div>
      <div class="photo g3" role="img" aria-label="Power lines and utility towers"></div>
      <div class="photo g4" role="img" aria-label="Railway transport corridor"></div>
    </div>
  </div>
</section>

<section class="partners">
  <h2>Our Partners</h2>
  <ul class="partner-list">
    <li>Ardelin</li>
    <li>Ovenra</li>
    <li>Dransvik</li>
    <li>Quorba</li>
    <li>Pelvaro</li>
  </ul>
</section>

<footer class="site-footer">
  <div class="wrap">
    <div class="footer-brand">
      <div class="brand"><span class="brand-mark"></span>VarnLink</div>
      <ul class="contact">
        <li><svg width="12" height="14" viewBox="0 0 12 14"><path d="M6 0a5 5 0 0 0-5 5c0 4 5 9 5 9s5-5 5-9a5 5 0 0 0-5-5z" fill="#bbb"/><circle cx="6" cy="5" r="2" fill="#2b2b2b"/></svg>12 Orrin Park, Victoria Australia 3999</li>
        <li><svg width="12" height="12" viewBox="0 0 12 12"><path d="M2 0h3l1 3-2 1a7 7 0 0 0 4 4l1-2 3 1v3a1 1 0 0 1-1 1A11 11 0 0 1 1 1a1 1 0 0 1 1-1z" fill="#bbb"/></svg>+61 3 5550 0142</li>
        <li><svg width="12" height="12" viewBox="0 0 12 12"><path d="M2 0h3l1 3-2 1a7 7 0 0 0 4 4l1-2 3 1v3a1 1 0 0 1-1 1A11 11 0 0 1 1 1a1 1 0 0 1 1-1z" fill="#bbb"/></svg>+61 3 5550 0179</li>
        <li><svg width="12" height="10" viewBox="0 0 12 10"><rect x="0.5" y="0.5" width="11" height="9" fill="none" stroke="#bbb"/><path d="M0.5 0.5 6 5l5.5-4.5" fill="none" stroke="#bbb"/></svg>info@varnlinkss.example</li>
      </ul>
    </div>
    <div class="footer-cols">
      <div><h3>Categories</h3><ul><li>Technology Partners</li><li>Industries</li><li>Professional Services</li><li>Rapid Site</li><li>Case Studies</li><li>Support</li><li>Products</li></ul></div>
      <div><h3>Recent Posts</h3><ul><li>This is a Gallery Post</li><li>Gallery Post</li><li>Standard Image Post</li><li>Image Post</li><li>Link Post</li></ul></div>
      <div><h3>Pages 1</h3><ul><li>About</li><li>FAQ</li><li>Responsibility</li><li>Contact</li></ul></div>
      <div><h3>Pages 2</h3><ul><li>Legal Information</li><li>Privacy Policy</li><li>Terms of Use</li><li>Careers</li><li>Site Map</li></ul></div>
    </div>
  </div>
</footer>

</body>
</html>
```